Talcum Powder Product Packaging - Brand Velvora Product Brisel

Talcum Powder Product packaging
Sophisticated Talcum Powder for Every Age
French Fragrance

Brand Name : Velvora
Product Name : Brisl
Product Pack : Measurement & Size Attached
Attached a Sample Product.

Looking for a Product Packaging for every age group.
Design Should be Aesthetic and Colorful . Target Market is all classes and all age group.
Updates

Project Deadline Extended
Reason: Need more colorful, modern designs

Target Market(s)

Upper Class

Industry/Entity Type

Product

Font styles to use
Decorative

Requirements
Must have
• Modern & Colorful - Use Dark Colors

```html
<!DOCTYPE html>
<html lang="en">
<head>
<meta charset="utf-8">
<title>Velvora Brisl Perfume Talc – Pack Wrap</title>
<link href="https://fonts.googleapis.com/css2?family=EB+Garamond:wght@400;500&family=Pinyon+Script&display=swap" rel="stylesheet">
<style>
  :root {
    --page: #ffffff;
    --cream: #f7e7a4;
    --bronze: #8f5d10;
    --bronze-soft: #c9a24f;
    --ink: #111111;
  }
  html, body {
    margin: 0;
    width: 1200px;
    height: 1200px;
    overflow: hidden;
    background: var(--page);
  }
  .canvas {
    position: relative;
    width: 1200px;
    height: 1200px;
  }
  .wrap-panel {
    position: absolute;
    left: 64px;
    top: 180px;
    width: 1078px;
    height: 844px;
    background: var(--cream);
    overflow: hidden;
  }
  .lace-top-edge {
    position: absolute;
    left: 0; top: 0;
    width: 100%; height: 20px;
    background: var(--bronze);
  }
  .lace-band-top {
    position: absolute;
    left: 0; top: 20px;
    width: 100%; height: 312px;
    background: linear-gradient(180deg, var(--bronze) 0%, var(--bronze-soft) 22%, #dcc27a 45%, var(--bronze) 62%, var(--bronze) 88%, var(--cream) 100%);
  }
  .lace-band-bottom {
    position: absolute;
    left: 0; bottom: 0;
    width: 100%; height: 62px;
    background: linear-gradient(180deg, var(--cream) 0%, var(--bronze-soft) 30%, var(--bronze) 100%);
  }
  .front-label {
    position: absolute;
    left: 654px;
    top: 330px;
    width: 424px;
    text-align: center;
    color: var(--ink);
    font-family: "EB Garamond", Garamond, serif;
  }
  .brand-name {
    position: absolute;
    left: 0; right: 0;
    top: 14px;
    margin: 0;
    font-size: 18px;
    font-weight: 500;
    letter-spacing: 0.3px;
  }
  .name-frame {
    position: absolute;
    left: 0;
    top: 57px;
    width: 424px;
    height: 222px;
  }
  .product-name {
    position: absolute;
    left: 0; right: 0;
    top: 118px;
    margin: 0;
    font-family: "Pinyon Script", cursive;
    font-size: 74px;
    font-weight: 400;
    line-height: 1;
  }
  .product-type {
    position: absolute;
    left: 0; right: 0;
    top: 298px;
    margin: 0;
    font-size: 18px;
  }
  .tagline {
    position: absolute;
    left: 0; right: 0;
    top: 412px;
    margin: 0;
    font-size: 17px;
  }
</style>
</head>
<body>
  <main class="canvas">
    <section class="wrap-panel">
      <div class="lace-top-edge"></div>
      <div class="lace-band-top" role="img" aria-label="Bronze lace border with scrolling floral motifs over a fine net"></div>
      <div class="lace-band-bottom" role="img" aria-label="Narrow bronze lace border with small scroll motifs"></div>

      <div class="front-label">
        <p class="brand-name">VELVORA</p>
        <svg class="name-frame" viewBox="0 0 424 222" role="img" aria-label="Oval name frame with bronze acanthus scrolls">
          <ellipse cx="212" cy="111" rx="208" ry="106" fill="none" stroke="var(--bronze)" stroke-width="4"/>
          <ellipse cx="212" cy="117" rx="180" ry="86" fill="none" stroke="var(--bronze)" stroke-width="2" opacity="0.55"/>
        </svg>
        <h1 class="product-name">Brisl</h1>
        <p class="product-type">Perfume Talc</p>
        <p class="tagline">Sensational Fragrance</p>
      </div>
    </section>
  </main>
</body>
</html>
```